Home Renovation Business needs a logo and business card design

I need a logo design for my home renovation company. I work hard to provide quality work for a fair price. I want a clean design that has something to make it pop and catch the eye. It should have somewhat of a modern feel to it. You can check out my website at www.kbbuildworks.com to see some examples of the type of work I do.
Updates

Hi Everyone,

For some reason, not all my information was posted. I would like the following contact information included in the design:

Phone: 365.417.9826        Email: kdrosmol@maplepost.ca        Website: www.kbbuildworks.com

Also, if you would like to include a list of the services I offer, then I'd like the card to be double sided. I provide the following services: Full kitchen, basement and bathroom renovations. Tile, laminate and hardwood installation. Decks, fences and sheds. Windows and doors.

Industry/Entity Type

Business

Requirements
Must have
• I want the following information listed on the card:
• KD Buildworks
• Kyle Drosmolen
• 365.417.9826
• kdrosmol@maplepost.ca
• www.kbbuildworks.com
Nice to have
• If you want you could also include the list of services I provide. If you include this list feel free to make the card double sided.
• Kitchen, bathroom and basement renovations
• Flooring installation
• Decks, fences and sheds
• Windows and doors
• I am not 100% sure if I want to include this on the card or not.

```html
<!DOCTYPE html>
<html lang="en">
<head>
<meta charset="utf-8">
<title>KD Buildworks – Business Card</title>
<link rel="stylesheet" href="https://fonts.googleapis.com/css2?family=Oswald:wght@500&family=Raleway:wght@300;400&display=swap">
<style>
  :root {
    --backdrop: #c9cacd;
    --card: #1e1a19;
    --card-edge: #2a2524;
    --accent: #b3191d;
    --light: #d6d6d6;
    --muted: #bdbdbd;
    --faint: #171413;
  }
  * { box-sizing: border-box; margin: 0; padding: 0; }
  html, body {
    width: 1200px; height: 900px; overflow: hidden;
    background: var(--backdrop);
  }
  .sheet {
    width: 1200px; height: 900px;
    display: flex; flex-direction: column; align-items: center; justify-content: center;
    gap: 56px;
  }
  .card {
    position: relative;
    width: 600px; height: 343px;
    background: var(--card);
    border: 1px solid var(--card-edge);
    box-shadow: 0 6px 18px rgba(0,0,0,.25);
    overflow: hidden;
  }

  /* Front */
  .card-front {
    display: flex; flex-direction: column; align-items: center;
    padding-top: 40px;
  }
  .brand {
    display: flex; flex-direction: column; align-items: center; gap: 14px;
  }
  .brand-square {
    display: block;
    width: 72px; height: 72px;
    border: 2px solid var(--accent);
  }
  .brand-name {
    font-family: "Oswald", sans-serif; font-weight: 500;
    font-size: 46px; letter-spacing: 0.5px; line-height: 1;
    color: var(--light); text-transform: uppercase;
    white-space: nowrap;
  }
  .contact-line {
    position: absolute; left: 0; right: 0; bottom: 44px;
    text-align: center;
    font-family: "Raleway", sans-serif; font-weight: 300;
    font-size: 15px; letter-spacing: 1px;
    color: var(--muted); text-transform: uppercase;
    white-space: nowrap;
  }
  .contact-line .divider { color: var(--accent); padding: 0 8px; }

  /* Back */
  .card-back { padding: 96px 0 0 44px; }
  .back-square {
    position: absolute; right: 40px; top: 36px;
    width: 260px; height: 260px;
    background: var(--faint);
    z-index: 0;
  }
  .back-text {
    position: relative; z-index: 1;
  }
  .services {
    list-style: none;
    font-family: "Raleway", sans-serif; font-weight: 400;
    font-size: 15px; line-height: 1.55;
    color: var(--muted);
    white-space: nowrap;
  }
  .website {
    margin-top: 20px;
    font-family: "Oswald", sans-serif; font-weight: 500;
    font-size: 26px; letter-spacing: 0.5px;
    color: var(--accent); text-transform: uppercase;
    white-space: nowrap;
  }
</style>
</head>
<body>
  <main class="sheet">
    <section class="card card-back" aria-label="Card back">
      <div class="back-square"></div>
      <div class="back-text">
        <ul class="services">
          <li>Full kitchen, Basement and Bathroom Renovations</li>
          <li>Tile, Laminate and Hardwood Installation</li>
          <li>Decks, Fences and Sheds</li>
          <li>Windows and Doors</li>
        </ul>
        <p class="website">www.kbbuildworks.com</p>
      </div>
    </section>

    <section class="card card-front" aria-label="Card front">
      <div class="brand">
        <span class="brand-square"></span>
        <span class="brand-name">KD Buildworks</span>
      </div>
      <p class="contact-line">
        Kyle Drosmolen<span class="divider">|</span>365.417.9826<span class="divider">|</span>kdrosmol@maplepost.ca
      </p>
    </section>
  </main>
</body>
</html>
```